Improved Business Card, Government Contracting

We are looking to update the design of our business cards. We would like to create a template that can be used for future employees and easy to update.

Halvorsen Advisory Partners, LLC is a Service Disabled Veteran Owned Small Business with headquarters located in Leavenworth, KS. Our current website is www.hapteam.com. We have contracts in KS and VA with expansion opportunities in various other states. Our primary line of work is within government contracting and providing consulting services to various organizations within the Bureau of Frontier Works. We would like to project a professional image of our company that is consistent with the industry. Provided are previous versions of our business card template that shows our logo as well. We would like to make sure the information on the cards are easily noticeable .

Target Market(s)

Government Officials
Fellow Small Business Contractors
Large Business Contractors (ex. TRUX, Keswell Barnaby, Pryde Okonjo Whitcombe)

Industry/Entity Type

Business

Contact Information for Business Card

Dale Fenwick
Office Manager
Halvorsen Advisory Partners
Ph: 913.555.0172
Email: d.fenwick@hapteam.us
www.hapteam.com

Requirements
Must have
• The business mailing address is:
• 31842 204th Lane
• Leavenworth, KS 66099
Nice to have
• Embossed lettering

```html
<!DOCTYPE html>
<html lang="en">
<head>
<meta charset="utf-8">
<title>Halvorsen Advisory Partners – Business Card</title>
<link href="https://fonts.googleapis.com/css2?family=Source+Sans+3:wght@400;600&family=Lato:wght@400&display=swap" rel="stylesheet">
<style>
  :root {
    --stage: #3a3a3a;
    --paper: #ffffff;
    --brand-blue: #3c58a8;
    --brand-blue-light: #6a84c4;
    --brand-yellow: #f6f05a;
    --ink: #4a4a4a;
    --rule: #8a8a8a;
  }
  * { margin: 0; padding: 0; box-sizing: border-box; }
  html, body { width: 1200px; height: 750px; overflow: hidden; }
  body {
    background: var(--stage);
    position: relative;
    font-family: "Source Sans 3", "Myriad Pro", sans-serif;
  }
  .card {
    position: absolute;
    top: 218px;
    width: 492px;
    height: 281px;
  }
  .card--front { left: 92px; background: var(--paper); }
  .card--back {
    left: 620px;
    background: radial-gradient(ellipse 55% 60% at 50% 40%, var(--brand-blue-light) 0%, var(--brand-blue) 100%);
  }

  .brand-name {
    position: absolute;
    display: flex;
    align-items: center;
    gap: 8px;
    font-weight: 600;
    line-height: 1.05;
    text-align: left;
  }
  .brand-mark { display: block; flex: none; }
  .card--front .brand-name {
    left: 36px; top: 122px;
    color: var(--brand-blue);
    font-size: 17px;
  }
  .card--front .brand-mark { width: 12px; height: 12px; background: var(--brand-blue); }
  .card--back .brand-name {
    left: 50%; top: 110px;
    transform: translateX(-50%);
    color: var(--brand-yellow);
    font-size: 29px;
    white-space: nowrap;
  }
  .card--back .brand-mark { width: 18px; height: 18px; background: var(--brand-yellow); }

  .divider {
    position: absolute;
    left: 246px; top: 30px;
    width: 1px; height: 222px;
    background: linear-gradient(to bottom, transparent, var(--rule) 20%, var(--rule) 80%, transparent);
  }

  .details {
    position: absolute;
    left: 285px; top: 52px;
    color: var(--ink);
    font-size: 11.5px;
    line-height: 15px;
  }
  .details__name {
    color: var(--brand-blue);
    font-weight: 600;
    font-size: 15.5px;
    line-height: 18px;
  }
  .details__address { margin-top: 18px; }
  .contact-list { list-style: none; margin-top: 15px; }
  .contact-list li {
    display: flex; align-items: center; gap: 8px;
    height: 15.8px;
    font-size: 12.5px;
  }
  .contact-list svg { width: 12px; height: 12px; fill: var(--brand-blue); flex: none; }

  .website {
    position: absolute;
    left: 0; right: 0; top: 234px;
    text-align: center;
    font-family: "Lato", sans-serif;
    font-size: 11.5px;
    letter-spacing: 1.4px;
    color: #ffffff;
  }
  .website__domain { color: var(--brand-yellow); }
</style>
</head>
<body>

<section class="card card--front">
  <div class="brand-name"><span class="brand-mark"></span><span>Halvorsen<br>Advisory Partners</span></div>
  <div class="divider"></div>
  <div class="details">
    <p class="details__name">Dale Fenwick</p>
    <p>Halvorsen Advisory Partners, LLC</p>
    <p>Office Manager</p>
    <p class="details__address">31842 204th Lane<br>Leavenworth, KS 66099</p>
    <ul class="contact-list">
      <li><svg viewBox="0 0 12 12"><path d="M1 4c0-2 2-3 5-3s5 1 5 3v1H8.5V3.8h-5V5H1z"/><path d="M3 6h6l1.5 5h-9z"/></svg>913.555.0172</li>
      <li><svg viewBox="0 0 12 12"><path d="M0.5 2.5h11v7h-11z M1.5 3.5v0.4L6 7l4.5-3.1v-0.4z" fill-rule="evenodd"/></svg>d.fenwick@hapteam.us</li>
      <li><svg viewBox="0 0 12 12"><path fill-rule="evenodd" d="M6 0.5a5.5 5.5 0 1 1 0 11a5.5 5.5 0 1 1 0-11zM6 1.5C5 2.6 4.6 4 4.5 5.5h3C7.4 4 7 2.6 6 1.5zM1.6 5.5h2C3.7 4 4 2.8 4.6 1.8A4.5 4.5 0 0 0 1.6 5.5zM10.4 5.5A4.5 4.5 0 0 0 7.4 1.8C8 2.8 8.3 4 8.4 5.5zM1.6 6.5a4.5 4.5 0 0 0 3 3.7C4 9.2 3.7 8 3.6 6.5zM4.5 6.5c.1 1.5.5 2.9 1.5 4c1-1.1 1.4-2.5 1.5-4zM8.4 6.5c-.1 1.5-.4 2.7-1 3.7a4.5 4.5 0 0 0 3-3.7z"/></svg>www.hapteam.com</li>
    </ul>
  </div>
</section>

<section class="card card--back">
  <div class="brand-name"><span class="brand-mark"></span><span>Halvorsen Advisory Partners</span></div>
  <p class="website">www.<span class="website__domain">hapteam</span>.com</p>
</section>

</body>
</html>
```